Business card Zottelgarten

Business card is for a self-employed dog trainer with own dog school. Name and logo of the dog school are available. Color specifications as well. The design should be classy and minimalist, but also modern. An already existing idea would be: Front: Only the logo Back: Contact data

Font styles to use
Serif
Sans Serif
Other font styles liked:
• Trajan Pro

Colors
f78f20

Requirements
Must have
• Name: Margit Wendler-Rasch Title: Dipl. Dog Trainer Contain my logo Follow my font and color preferences (see files)

```html
<!DOCTYPE html>
<html lang="en">
<head>
<meta charset="utf-8">
<title>Zottelgarten – Business Card</title>
<link rel="stylesheet" href="https://fonts.googleapis.com/css2?family=Cinzel:wght@400;500&display=swap">
<style>
  :root {
    --backdrop: #ece8e3;
    --card: #7a6a5a;
    --ink: #ffffff;
    --shadow: rgba(60, 45, 30, 0.25);
  }
  * { box-sizing: border-box; margin: 0; padding: 0; }
  html, body {
    width: 1200px;
    height: 1200px;
    overflow: hidden;
    background: var(--backdrop);
  }
  .canvas {
    position: relative;
    width: 1200px;
    height: 1200px;
    font-family: "Cinzel", "Trajan Pro", serif;
    color: var(--ink);
  }
  .card {
    position: absolute;
    left: 148px;
    width: 904px;
    height: 516px;
    background: var(--card);
    box-shadow: 0 6px 18px var(--shadow);
  }
  .card--front {
    top: 52px;
    border-radius: 0 258px 258px 0;
  }
  .card--back {
    top: 618px;
    border-radius: 258px 0 0 258px;
  }
  .wordmark {
    position: absolute;
    text-align: left;
  }
  .wordmark__name {
    display: block;
    font-weight: 400;
    text-transform: uppercase;
    line-height: 1;
    white-space: nowrap;
  }
  .wordmark__url {
    display: block;
    text-transform: uppercase;
    line-height: 1;
    white-space: nowrap;
  }
  .card--front .wordmark { left: 44px; top: 50px; }
  .card--front .wordmark__name { font-size: 36px; letter-spacing: 1px; }
  .card--front .wordmark__url { font-size: 10px; letter-spacing: 6.2px; margin-top: 5px; }

  .card--back .wordmark {
    left: 0;
    right: 0;
    top: 362px;
    text-align: center;
  }
  .card--back .wordmark__name { font-size: 48px; letter-spacing: 3px; }
  .card--back .wordmark__url { font-size: 14px; letter-spacing: 10px; margin-top: 8px; }

  .emblem {
    position: absolute;
    display: block;
  }
  .card--front .emblem { left: 412px; top: 18px; width: 480px; height: 480px; }
  .card--back .emblem { left: 316px; top: 82px; width: 264px; height: 264px; }

  .person {
    position: absolute;
    left: 44px;
    top: 226px;
    width: 350px;
  }
  .person__name {
    font-size: 23px;
    font-weight: 500;
    line-height: 1.1;
    letter-spacing: 0;
    white-space: nowrap;
  }
  .person__title {
    font-size: 19px;
    line-height: 1.3;
    white-space: nowrap;
  }
  .contact {
    position: absolute;
    left: 44px;
    top: 386px;
    width: 350px;
    list-style: none;
    font-size: 16px;
    letter-spacing: 0.2px;
  }
  .contact__item {
    display: flex;
    align-items: center;
    gap: 10px;
    height: 32px;
    white-space: nowrap;
  }
  .contact__icon { width: 17px; height: 17px; fill: var(--ink); flex: none; }
</style>
</head>
<body>
<main class="canvas">

  <section class="card card--front" aria-label="Card front">
    <div class="wordmark">
      <span class="wordmark__name">Zottelgarten</span>
      <span class="wordmark__url">www.zottelgarten.example</span>
    </div>

    <div class="person">
      <p class="person__name">MARGIT WENDLER-RASCH</p>
      <p class="person__title">Dipl. Dog Trainer</p>
    </div>

    <ul class="contact">
      <li class="contact__item">Lindenweg 12, Bergdorf</li>
      <li class="contact__item">
        <svg class="contact__icon" viewBox="0 0 24 24" aria-hidden="true"><path d="M6.6 10.8a15.1 15.1 0 0 0 6.6 6.6l2.2-2.2a1 1 0 0 1 1-.25 11.4 11.4 0 0 0 3.6.57 1 1 0 0 1 1 1V20a1 1 0 0 1-1 1A17 17 0 0 1 3 4a1 1 0 0 1 1-1h3.5a1 1 0 0 1 1 1 11.4 11.4 0 0 0 .57 3.6 1 1 0 0 1-.25 1z"/></svg>
        000-555-0142
      </li>
      <li class="contact__item">
        <svg class="contact__icon" viewBox="0 0 24 24" aria-hidden="true"><path d="M2 5h20v14H2z M2 5l10 8 10-8" fill="none" stroke="#fff" stroke-width="2"/></svg>
        INFO@ZOTTELGARTEN.EXAMPLE
      </li>
    </ul>

    <svg class="emblem" viewBox="0 0 100 100" role="img" aria-label="Logo area of the dog school">
      <circle cx="50" cy="50" r="49" fill="var(--ink)"/>
    </svg>
  </section>

  <section class="card card--back" aria-label="Card back">
    <svg class="emblem" viewBox="0 0 100 100" role="img" aria-label="Logo area of the dog school">
      <circle cx="50" cy="50" r="49" fill="var(--ink)"/>
    </svg>
    <div class="wordmark">
      <span class="wordmark__name">Zottelgarten</span>
      <span class="wordmark__url">www.zottelgarten.example</span>
    </div>
  </section>

</main>
</body>
</html>
```